Clean business card with logo provided

I want a card that will stand out among the masses. I need the color and image to show professionalism and yet have a family appeal showing that I only deal with win/win scenarios. The back of the card will be used to take notes about the individual so I can use that in my database entry. I like modern design but need professionalism in it also. It needs to fit my "clean, safe, and affordable housing" motto. I need to be able to write on the file and update the card details for my employees.

Target Market(s)

Investors looking to make investment income through real estate

Industry/Entity Type

Real Estate

Contact Information for Business Card

Troy Vandemark
blank address, city, st, zip code
480-555-0147
troyvandemark@quillrentals.example
www.quillrentals.example

Font styles to use
Sans Serif

Requirements
Must have
• I would like the back of the card to have lines for info. example
• Met/Visited: Date:
• Interets:
Nice to have
• I want the cards color to match the logo background color. Font with details to be san serif and black. I want the card rectangular with square corners. Standard business card size. I would like to see cards designed with both images to see which i prefer more.

```html
<!DOCTYPE html>
<html lang="en">
<head>
<meta charset="utf-8">
<title>Quill Rentals LLC – Business Card</title>
<link rel="stylesheet" href="https://fonts.googleapis.com/css2?family=Open+Sans:wght@400;600&display=swap">
<style>
  :root {
    --canvas-bg: #e9e7e3;
    --brand-cyan: #1bb3cc;
    --card-black: #060708;
    --card-white: #ffffff;
    --ink-dark: #1d1d1d;
    --rule-grey: #8e8e8e;
    --text-light: #ffffff;
  }
  * { box-sizing: border-box; margin: 0; padding: 0; }
  html, body {
    width: 1200px; height: 1200px; overflow: hidden;
    background: var(--canvas-bg);
    font-family: "Open Sans", Arial, sans-serif;
  }
  .stage {
    width: 1200px; height: 1200px;
    display: flex; flex-direction: column; align-items: center; justify-content: center;
    gap: 60px;
  }
  .card {
    position: relative;
    width: 900px; height: 514px;
    box-shadow: 0 6px 18px rgba(0,0,0,.18);
  }
  address { font-style: normal; }

  /* Note-taking back side */
  .card--notes {
    background: var(--brand-cyan);
    padding: 22px;
  }
  .notes-panel {
    position: relative;
    width: 100%; height: 100%;
    background: var(--card-white);
    color: var(--ink-dark);
  }
  .note-row {
    position: absolute; left: 40px; right: 40px;
    display: flex; align-items: flex-end;
    font-size: 25px;
  }
  .note-row__label { width: 270px; }
  .note-row__colon { width: 30px; }
  .note-row__line { flex: 1; border-bottom: 2px solid var(--rule-grey); margin-bottom: 8px; }
  .note-row--date { top: 44px; }
  .note-row--interests { top: 110px; }
  .note-row--problems { top: 176px; }
  .blank-line {
    position: absolute; left: 40px; height: 0;
    border-bottom: 2px solid var(--rule-grey);
  }
  .blank-line--full { top: 268px; right: 40px; }
  .blank-line--short { top: 326px; width: 300px; }
  .notes-address {
    position: absolute; left: 40px; bottom: 30px;
    font-size: 22px; line-height: 1.3;
  }

  /* Brand lockup */
  .brand {
    position: absolute;
    display: flex; flex-direction: column; align-items: flex-end;
  }
  .brand__name {
    display: flex; align-items: center; gap: 14px;
    font-weight: 600; font-size: 44px; letter-spacing: 3px;
    color: var(--brand-cyan);
    text-transform: uppercase;
    white-space: nowrap;
  }
  .brand__dot {
    width: 30px; height: 30px; border-radius: 50%;
    background: var(--brand-cyan);
  }
  .brand__tagline {
    margin-top: 6px;
    font-size: 17px; color: var(--brand-cyan);
    white-space: nowrap;
  }
  .card--notes .brand { right: 40px; bottom: 36px; }
  .card--notes .brand__name { font-size: 34px; letter-spacing: 2px; }
  .card--notes .brand__dot { width: 24px; height: 24px; }
  .card--notes .brand__tagline { font-size: 15px; }
  .card--contact .brand { right: 50px; top: 50px; }

  /* Contact front side */
  .card--contact {
    background: var(--card-black);
    color: var(--text-light);
  }
  .holder {
    position: absolute; left: 60px; bottom: 56px;
  }
  .holder__name { font-size: 36px; }
  .holder__title { font-size: 24px; color: var(--brand-cyan); margin-bottom: 26px; }
  .holder__detail { font-size: 24px; line-height: 1.35; }
  .contact-address {
    position: absolute; right: 50px; top: 250px;
    text-align: right; font-size: 24px; line-height: 1.35;
  }
</style>
</head>
<body>
<main class="stage">

  <section class="card card--notes" aria-label="Card back for notes">
    <div class="notes-panel">
      <div class="note-row note-row--date">
        <span class="note-row__label">Met / Visited: Date</span>
        <span class="note-row__colon">:</span>
        <span class="note-row__line"></span>
      </div>
      <div class="note-row note-row--interests">
        <span class="note-row__label">Interets</span>
        <span class="note-row__colon">:</span>
        <span class="note-row__line"></span>
      </div>
      <div class="note-row note-row--problems">
        <span class="note-row__label">Problems</span>
        <span class="note-row__colon">:</span>
        <span class="note-row__line"></span>
      </div>
      <div class="blank-line blank-line--full"></div>
      <div class="blank-line blank-line--short"></div>

      <address class="notes-address">
        blank address,<br>empty city,<br>state zonk, 12345
      </address>

      <div class="brand">
        <div class="brand__name"><span>Quill Rentals LLC</span><span class="brand__dot"></span></div>
        <div class="brand__tagline">Providing clean, safe and affordable housing</div>
      </div>
    </div>
  </section>

  <section class="card card--contact" aria-label="Card front with contact details">
    <div class="brand">
      <div class="brand__name"><span>Quill Rentals LLC</span><span class="brand__dot"></span></div>
      <div class="brand__tagline">Providing clean, safe and affordable housing</div>
    </div>

    <address class="contact-address">
      blank address,<br>empty city,<br>state zonk, 12345
    </address>

    <div class="holder">
      <div class="holder__name">Troy Vandemark</div>
      <div class="holder__title">CEO</div>
      <div class="holder__detail">480-555-0147</div>
      <div class="holder__detail">troyvandemark@quillrentals.example</div>
      <div class="holder__detail">www.quillrentals.example</div>
    </div>
  </section>

</main>
</body>
</html>
```